Postcard Design

Books for sale targeting doctors and patients.

Target Market(s)

Medically challenged individuals and doctors

Font styles to use
Serif

Colors

Designer to choose colors to be used in the design.

Requirements
Must have
• see attached
Nice to have
• see attached

```html
<!DOCTYPE html>
<html lang="en">
<head>
<meta charset="utf-8">
<title>Recovery Postcard – Back</title>
<link rel="stylesheet" href="https://fonts.googleapis.com/css2?family=Carlito:wght@400;700&family=Share+Tech+Mono&display=swap">
<style>
  :root {
    --paper: #ffffff;
    --ink: #000000;
    --frame: #1a1a1a;
  }
  html, body {
    margin: 0;
    padding: 0;
    width: 1200px;
    height: 916px;
    overflow: hidden;
    background: var(--paper);
  }
  .postcard {
    position: relative;
    width: 1200px;
    height: 916px;
    background: var(--paper);
    color: var(--ink);
    font-family: "Carlito", "Calibri", sans-serif;
  }
  .quote {
    position: absolute;
    left: 30px;
    top: 78px;
    width: 620px;
    margin: 0;
    font-weight: 700;
    font-size: 21.5px;
    line-height: 62.5px;
  }
  .quote p { margin: 0; }
  .quote-author {
    position: absolute;
    left: 30px;
    top: 328px;
    margin: 0;
    font-weight: 700;
    font-size: 21.5px;
    line-height: 30px;
  }
  .stamp-box {
    position: absolute;
    left: 956px;
    top: 79px;
    width: 130px;
    height: 144px;
    border: 2px solid var(--frame);
    box-sizing: border-box;
    text-align: center;
    font-size: 16.5px;
  }
  .stamp-box span {
    position: absolute;
    left: 0;
    right: 0;
  }
  .stamp-box .stamp-word { top: 17px; }
  .stamp-box .here-word { top: 65px; }
  .mailing-address {
    position: absolute;
    left: 655px;
    top: 398px;
    margin: 0;
    font-family: "Share Tech Mono", "Courier New", monospace;
    font-size: 29px;
    line-height: 46.5px;
    letter-spacing: 1.6px;
  }
  .contact {
    position: absolute;
    left: 60px;
    top: 788px;
    margin: 0;
    font-size: 21px;
    line-height: 35px;
  }
  .contact strong { font-weight: 700; }
</style>
</head>
<body>
  <main class="postcard">
    <blockquote class="quote">
      <p>“Anyone who has experienced a life-changing medical<br>
      event can relate. It’s easy to become discouraged. I just<br>
      want to share the message, ‘don’t give up.’ Keep working<br>
      toward recovery, one day at a time.”</p>
    </blockquote>
    <p class="quote-author">~ Daniel R. Whitcomb</p>

    <div class="stamp-box">
      <span class="stamp-word">Stamp</span>
      <span class="here-word">Here</span>
    </div>

    <address class="mailing-address">
      Mailing Address Line 1<br>
      Mailing Address Line 2<br>
      Mailing Address Line 3<br>
      Mailing Address Line 4<br>
      Mailing Address Line 5
    </address>

    <p class="contact">
      <strong>Email:</strong> dwhitcomb@healthpathwaysdaily.com<br>
      <strong>Phone:</strong> (555) 318-2704
    </p>
  </main>
</body>
</html>
```